Help us Create Excitement with a Food To Go Web Site Menu

We are seeking a design that can serve as a template for a Wordpress based website. The template will present the name (BrimBowl), present the menu items with price details, and contact details. The final design should NOT have the Mingle Kerb Eats subtitle anywhere in the site.
Our plan is to have the menu with basic graphic elements with the options to link to images/pictures of the menu item (perhaps linked via Instagram or something like that if possible).
Updates

Target Market(s)

Home dining menu intended to offer perspective customers an understanding of what they will be enjoying.

Contact Information for Business Card

BrimBowl logo (without the Mingle Kerb Eats tag line included)
hi@brimbowl.com.au
Phone: XXXX XXX XXX (to be provided)

Coding

Coded - Design and coding required

Number of Pages Required

2 page

Requirements
Must have
• A bold and colourful presence that is also on the playful side.

A clearly readable menu layout that doesn't feel small based on the limited number of items that we offer at this time.
Nice to have
• A playful semi-graffiti based feel would be nice to convey a sense of playfulness.
Should not have
• The design should not have an overly Asian feel to it.

It appears many people are misreading the brief so I am adding this point to clarify one of the design requirements.
-- The final design should NOT have the Mingle Kerb Eats subtitle anywhere in the site, including the logo.

```html
<!DOCTYPE html>
<html lang="en">
<head>
<meta charset="utf-8">
<title>BrimBowl — Menu</title>
<link href="https://fonts.googleapis.com/css2?family=Poppins:wght@400;500;600;700;800&display=swap" rel="stylesheet">
<style>
:root{
  --red:#e8141a;
  --deep-red:#8e0d10;
  --ink:#1d1d1d;
  --text:#3a3a3a;
  --muted:#6b6b6b;
  --white:#ffffff;
  --charcoal:#232323;
  --field:#5a5050;
}
*{box-sizing:border-box;margin:0;padding:0}
html,body{width:1200px;height:3712px;overflow:hidden}
body{font-family:'Poppins',sans-serif;color:var(--text);background:var(--white);position:relative}

/* Header */
.site-header{position:absolute;left:0;top:0;width:1200px;height:100px;z-index:3}
.brand{position:absolute;left:36px;top:28px;display:flex;align-items:center;gap:10px;font-weight:800;font-size:38px;line-height:1;color:var(--red);letter-spacing:-1px}
.brand-dot{width:20px;height:20px;background:var(--ink);border-radius:50%}
.main-nav{position:absolute;right:56px;top:36px;display:flex;gap:40px;align-items:center;font-size:18px;font-weight:500;color:var(--ink)}
.main-nav .active{background:var(--red);color:var(--white);padding:5px 20px;border-radius:20px}

/* Hero */
.hero{position:absolute;left:0;top:0;width:1200px;height:870px}
.hero-area{position:absolute;left:0;top:0;width:1200px;height:870px}
.hero-copy{position:absolute;left:0;top:524px;width:1200px;text-align:center;color:var(--white);z-index:2}
.hero-kicker{font-size:30px;font-weight:600;letter-spacing:1px;line-height:1.2}
.hero-title{font-size:30px;font-weight:600;margin-top:8px;display:flex;justify-content:center;align-items:center;gap:12px;line-height:1}
.hero-title strong{font-size:50px;font-weight:800}
.hero-title .pay{font-size:13px;font-weight:700;line-height:1.1;text-align:left}
.hero-btn{display:inline-block;margin-top:22px;background:var(--red);color:var(--white);font-size:18px;font-weight:600;padding:8px 28px;border-radius:22px}

/* Menu intro */
.menu-intro{position:absolute;left:0;top:868px;width:1200px;text-align:center;line-height:1.2}
.menu-intro h2{font-size:40px;font-weight:500;color:var(--ink)}
.menu-intro h2 span{display:block;color:var(--red);font-weight:700;font-size:42px}

/* Menu cards */
.menu-card{position:absolute;width:392px;height:556px;background:var(--white);box-shadow:0 4px 18px rgba(0,0,0,.18);overflow:hidden}
.menu-card.featured{background:var(--red);color:var(--white)}
.card-photo{position:absolute;left:0;top:0;width:100%;height:240px;
  clip-path:polygon(0 0,100% 0,100% 86%,93% 92%,85% 88%,76% 95%,66% 90%,57% 97%,46% 91%,37% 96%,27% 90%,18% 95%,9% 89%,0 94%)}
.card-body{position:absolute;left:32px;right:32px;top:272px}
.card-body h3{font-size:26px;font-weight:700;color:var(--red)}
.featured .card-body h3{color:var(--white)}
.card-body p{font-size:15px;line-height:1.6;margin-top:12px;color:var(--muted)}
.featured .card-body p{color:var(--white)}
.card-foot{position:absolute;left:32px;right:32px;bottom:36px;display:flex;align-items:center;justify-content:space-between}
.price{font-size:26px;font-weight:700;color:var(--ink)}
.price.small{font-size:17px;line-height:1.15}
.featured .price{color:var(--white)}
.order-btn{display:flex;align-items:center;gap:8px;border:2px solid var(--red);color:var(--red);background:var(--white);border-radius:22px;padding:6px 20px;font-size:15px;font-weight:600}
.fav-btn{width:46px;height:46px;border-radius:50%;background:var(--deep-red);display:flex;align-items:center;justify-content:center}
.featured .fav-btn{background:var(--white)}

/* Contact */
.contact{position:absolute;left:0;top:2300px;width:1200px;height:470px;
  background:radial-gradient(circle at 70% 55%,#c9a15a 0%,#8b6a33 30%,#3b2c1a 70%,#1d150d 100%);
  clip-path:polygon(0 4%,8% 1%,18% 5%,30% 0,42% 4%,55% 1%,68% 5%,80% 0,92% 4%,100% 1%,100% 96%,90% 100%,78% 95%,64% 99%,50% 95%,36% 100%,22% 96%,10% 99%,0 95%)}
.contact-form{position:absolute;left:328px;top:84px;width:540px}
.contact-form h2{font-size:40px;font-weight:600;color:var(--white);margin-bottom:20px;line-height:1.2}
.form-row{display:flex;gap:16px;margin-bottom:16px}
.field{flex:1;height:44px;background:var(--field);opacity:.92;color:#d8d0d0;font-size:14px;padding:10px 14px}
.field.message{height:104px}
.send-btn{display:block;width:130px;margin:20px auto 0;background:var(--red);color:var(--white);text-align:center;font-size:16px;font-weight:600;padding:8px 0;border-radius:20px}

/* Instagram */
.instagram{position:absolute;left:256px;top:2870px;width:690px}
.instagram h2{font-size:36px;font-weight:700;color:var(--ink);line-height:1.2}
.instagram p{font-size:15px;line-height:1.55;color:var(--muted);margin-top:8px;width:600px}
.insta-grid{position:absolute;left:0;top:124px;width:690px;height:296px;display:grid;grid-template-columns:312px 180px 170px;grid-template-rows:144px 144px;gap:8px 14px}
.insta-grid .tile:first-child{grid-row:1 / 3}

/* Footer */
.site-footer{position:absolute;left:0;top:3396px;width:1200px;height:316px;background:var(--charcoal);color:#cfcfcf;
  clip-path:polygon(0 5%,10% 1%,22% 4%,34% 0,46% 5%,58% 1%,70% 4%,82% 0,94% 5%,100% 2%,100% 100%,0 100%)}
.foot-col{position:absolute;top:72px;font-size:14px;line-height:1.9}
.foot-col h4{font-size:15px;font-weight:600;color:var(--white);letter-spacing:.5px;margin-bottom:10px}
.foot-line{display:flex;align-items:center;gap:10px}
.subscribe{display:flex;margin-top:12px}
.subscribe .email{width:170px;height:36px;background:var(--white);color:#999;font-size:13px;padding:8px 12px;border-radius:18px 0 0 18px}
.subscribe .go{height:36px;background:var(--red);color:var(--white);font-size:13px;font-weight:600;padding:8px 16px;border-radius:0 18px 18px 0}
.foot-rule{position:absolute;left:120px;right:120px;top:238px;border-top:1px solid #4a4a4a}
.copyright{position:absolute;left:120px;top:262px;font-size:13px}
.social{position:absolute;right:120px;top:264px;display:flex;gap:14px}
.social span{width:14px;height:14px;border-radius:50%;background:#9a9a9a}
</style>
</head>
<body>

<section class="hero">
  <svg class="hero-area" viewBox="0 0 1200 870" preserveAspectRatio="none" role="img" aria-label="Bowl of beef noodle soup with fresh herbs, seen from above">
    <defs>
      <linearGradient id="heroTone" x1="0" y1="0" x2="1" y2="1">
        <stop offset="0" stop-color="#4a5530"/>
        <stop offset="0.5" stop-color="#2e3320"/>
        <stop offset="1" stop-color="#1a1a16"/>
      </linearGradient>
    </defs>
    <polygon fill="url(#heroTone)" points="170,110 240,86 330,100 420,70 520,90 620,64 720,88 820,70 920,92 1010,76 1110,96 1200,80 1200,840 1150,852 1080,836 1000,856 920,840 840,860 760,842 680,862 600,844 520,860 440,842 360,858 290,838 220,852 160,820 130,760 150,690 110,620 140,540 100,460 130,380 90,300 130,220 110,160"/>
  </svg>
  <div class="hero-copy">
    <div class="hero-kicker">DISCOVER WHAT'S NEW</div>
    <div class="hero-title">AND <strong>ORDER</strong> WITH <span class="pay">PAY<br>SWIFT</span> <strong>ONLINE</strong></div>
    <span class="hero-btn">Our Menu</span>
  </div>
</section>

<header class="site-header">
  <div class="brand"><span class="brand-dot"></span>BrimBowl</div>
  <nav class="main-nav">
    <span class="active">BrimBowl</span>
    <span>The Menu</span>
    <span>Price Details</span>
    <span>Contact</span>
  </nav>
</header>

<section class="menu-intro">
  <h2>What Makes <span>Our Menus Special ?</span></h2>
</section>

<article class="menu-card" style="left:180px;top:1008px">
  <div class="card-photo" role="img" aria-label="Beef noodle soup photo" style="background:linear-gradient(135deg,#3a3a2a,#7c8a4a 50%,#2a2a22)"></div>
  <div class="card-body">
    <h3>Beef Noodle Soup</h3>
    <p>Just like Nana used to make. Our soup simmers for 12 hours. We boil and reduce our own broth, using the freshest, locally sourced ingredients.</p>
  </div>
  <div class="card-foot">
    <span class="price">$14</span>
    <span class="order-btn"><svg width="16" height="16" viewBox="0 0 16 16"><path d="M1 2h2l2 8h8l2-6H4" fill="none" stroke="currentColor" stroke-width="1.6"/><circle cx="6" cy="13.5" r="1.3" fill="currentColor"/><circle cx="12" cy="13.5" r="1.3" fill="currentColor"/></svg>Add to Order</span>
    <span class="fav-btn"><svg width="22" height="22" viewBox="0 0 16 16"><path d="M1 2h2l2 8h8l2-6H4" fill="none" stroke="#fff" stroke-width="1.6"/><circle cx="6" cy="13.5" r="1.3" fill="#fff"/><circle cx="12" cy="13.5" r="1.3" fill="#fff"/></svg></span>
  </div>
</article>

<article class="menu-card featured" style="left:628px;top:1008px">
  <div class="card-photo" role="img" aria-label="Egg rolls on a plate photo" style="background:linear-gradient(135deg,#4b6a34,#b07a6a 50%,#7a5a4a)"></div>
  <div class="card-body">
    <h3>Egg Rolls</h3>
    <p>Our egg rolls are an experience not to be missed. They are provided either prepared and ready to eat or fresh and ready for pan-frying at your convenience.</p>
  </div>
  <div class="card-foot">
    <span class="price">$10</span>
    <span class="order-btn"><svg width="16" height="16" viewBox="0 0 16 16"><path d="M1 2h2l2 8h8l2-6H4" fill="none" stroke="currentColor" stroke-width="1.6"/><circle cx="6" cy="13.5" r="1.3" fill="currentColor"/><circle cx="12" cy="13.5" r="1.3" fill="currentColor"/></svg>Add to Order</span>
    <span class="fav-btn"><svg width="22" height="22" viewBox="0 0 16 16"><path d="M1 2h2l2 8h8l2-6H4" fill="none" stroke="#e8141a" stroke-width="1.6"/><circle cx="6" cy="13.5" r="1.3" fill="#e8141a"/><circle cx="12" cy="13.5" r="1.3" fill="#e8141a"/></svg></span>
  </div>
</article>

<article class="menu-card" style="left:180px;top:1620px">
  <div class="card-photo" role="img" aria-label="Crab soup photo" style="background:linear-gradient(135deg,#d9b98a,#f0dfc4 50%,#c89a5e)"></div>
  <div class="card-body">
    <h3>Crab Soup</h3>
    <p>We use fresh whole crunch crab meat served in a thick homemade chicken and pork bone based broth that takes 8 hours to prepare.</p>
  </div>
  <div class="card-foot">
    <span class="price small">Market<br>Price</span>
    <span class="order-btn"><svg width="16" height="16" viewBox="0 0 16 16"><path d="M1 2h2l2 8h8l2-6H4" fill="none" stroke="currentColor" stroke-width="1.6"/><circle cx="6" cy="13.5" r="1.3" fill="currentColor"/><circle cx="12" cy="13.5" r="1.3" fill="currentColor"/></svg>Add to Order</span>
    <span class="fav-btn"><svg width="22" height="22" viewBox="0 0 16 16"><path d="M1 2h2l2 8h8l2-6H4" fill="none" stroke="#fff" stroke-width="1.6"/><circle cx="6" cy="13.5" r="1.3" fill="#fff"/><circle cx="12" cy="13.5" r="1.3" fill="#fff"/></svg></span>
  </div>
</article>

<article class="menu-card" style="left:628px;top:1620px">
  <div class="card-photo" role="img" aria-label="Tuna salad sandwich photo" style="background:linear-gradient(180deg,#2a2a2a,#e3c79a 45%,#f3e6cf 60%,#2a2a2a)"></div>
  <div class="card-body">
    <h3>Tuna Salad Sandwich</h3>
    <p>Just like Nana used to make. Our bread takes 12 hours to make. We bake and fill our own loaves, using the freshest, locally sourced ingredients.</p>
  </div>
  <div class="card-foot">
    <span class="price">$14</span>
    <span class="order-btn"><svg width="16" height="16" viewBox="0 0 16 16"><path d="M1 2h2l2 8h8l2-6H4" fill="none" stroke="currentColor" stroke-width="1.6"/><circle cx="6" cy="13.5" r="1.3" fill="currentColor"/><circle cx="12" cy="13.5" r="1.3" fill="currentColor"/></svg>Add to Order</span>
    <span class="fav-btn"><svg width="22" height="22" viewBox="0 0 16 16"><path d="M1 2h2l2 8h8l2-6H4" fill="none" stroke="#fff" stroke-width="1.6"/><circle cx="6" cy="13.5" r="1.3" fill="#fff"/><circle cx="12" cy="13.5" r="1.3" fill="#fff"/></svg></span>
  </div>
</article>

<section class="contact" role="img" aria-label="Close-up of a spoon lifting noodles from a bowl of soup">
  <form class="contact-form">
    <h2>Get In Touch</h2>
    <div class="form-row"><div class="field">Name</div><div class="field">Email</div></div>
    <div class="form-row"><div class="field message">Message</div></div>
    <span class="send-btn">Send Now</span>
  </form>
</section>

<section class="instagram">
  <h2>Instagram</h2>
  <p>Meet your fellow diners! Show us your dish style on social media and tag @BRIMBOWL for a chance to win free items and be featured on our site!</p>
  <div class="insta-grid">
    <div class="tile" role="img" aria-label="Friends sharing a meal at a table" style="background:linear-gradient(135deg,#8a4a3a,#c98a5a)"></div>
    <div class="tile" role="img" aria-label="Grilled meat dish" style="background:linear-gradient(135deg,#5a3a3a,#a0706a)"></div>
    <div class="tile" role="img" aria-label="Crab soup bowl" style="background:linear-gradient(135deg,#d8a86a,#f0d8b0)"></div>
    <div class="tile" role="img" aria-label="Sandwich halves" style="background:linear-gradient(135deg,#c8a070,#f0e0c0)"></div>
    <div class="tile" role="img" aria-label="Noodle soup with herbs" style="background:linear-gradient(135deg,#4a5a2a,#9a8a5a)"></div>
  </div>
</section>

<footer class="site-footer">
  <div class="foot-col" style="left:120px">
    <h4>CONTACT US</h4>
    <div class="foot-line"><svg width="12" height="14" viewBox="0 0 12 14"><path d="M6 13S1 8 1 5a5 5 0 0 1 10 0c0 3-5 8-5 8z" fill="#cfcfcf"/><circle cx="6" cy="5" r="1.8" fill="#232323"/></svg>Adress / Legal</div>
    <div style="padding-left:22px;margin-top:-6px">Country Name, Street</div>
    <div class="foot-line"><svg width="12" height="12" viewBox="0 0 12 12"><path d="M2 1h2.5l1 3-1.5 1a6 6 0 0 0 3 3l1-1.5 3 1V11A10 10 0 0 1 1 2z" fill="#cfcfcf"/></svg>+123 4567 8900</div>
    <div class="foot-line"><svg width="13" height="10" viewBox="0 0 13 10"><rect x=".5" y=".5" width="12" height="9" fill="none" stroke="#cfcfcf"/><path d="M.5.5l6 5 6-5" fill="none" stroke="#cfcfcf"/></svg>hi@brimbowl.com.au</div>
  </div>
  <div class="foot-col" style="left:400px">
    <h4>QUICK LINKS</h4>
    <div>Home</div><div>BrimBowl</div><div>The Menu</div>
  </div>
  <div class="foot-col" style="left:580px">
    <h4>QUICK LINKS</h4>
    <div>Price Details</div><div>Order Now</div><div>Contact Us</div>
  </div>
  <div class="foot-col" style="left:780px;width:300px">
    <h4>WRITE TO US</h4>
    <div style="line-height:1.5">Provide your email below to subscribe to our newsletter</div>
    <div class="subscribe"><span class="email">Email address</span><span class="go">Subscribe</span></div>
  </div>
  <div class="foot-rule"></div>
  <div class="copyright">Copyright 2024 BrimBowl</div>
  <div class="social"><span></span><span></span><span></span><span></span><span></span></div>
</footer>

</body>
</html>
```